Pinecrest Renovations - Get the creative juices going!!

Pinecrest does not do the actual renovation work. The company provides high end project management of renovation (primarily residential - with an eye toward commercial) The renovation work could look very different between projects. This company manages the work of contractors, architects and interior designers (either subcontracted directly by Pinecrest or hired by the client and entrusted to Pinecrest to manage). Clients are high end in the economic scale and the card needs to have a high end feel to it.

The owner is female, but the audience will be heavily slanted male. It should not be a "feminine" or "masculine" looking card. If anything, slant more on the masculine side. Clean, simple, yet creative and artistically appealing. The card design should complement and in no way compete with the logo.

When people think of our company: trust, integrity, dynamic, limitless possibilities, transition, energy, creative. We plan to expand in the future to be international.

There will also be a contest running for stationary. Please check that section, as well.

***Black is 80-90 percent black. Not stark black

Tight timeline. Needs cards printed quickly!

Residential

```html
<!DOCTYPE html>
<html lang="en">
<head>
<meta charset="utf-8">
<title>Pinecrest Renovations – Business Card</title>
<link href="https://fonts.googleapis.com/css2?family=Open+Sans:wght@400;600;700&display=swap" rel="stylesheet">
<style>
  :root {
    --page-bg: #e9e7e4;
    --card-white: #ffffff;
    --teal: #1fa99a;
    --ink: #2e3032;
    --band-dark: #2a2c2e;
    --text-dark: #333537;
  }
  * { box-sizing: border-box; margin: 0; padding: 0; }
  html, body {
    width: 1200px; height: 800px; overflow: hidden;
    background: var(--page-bg);
    font-family: "Open Sans", Arial, sans-serif;
  }
  .card {
    position: absolute; left: 100px; top: 100px;
    width: 1000px; height: 600px;
    background: var(--card-white);
    box-shadow: 0 18px 40px rgba(0,0,0,0.18);
    overflow: hidden;
  }
  .brand {
    position: absolute; left: 90px; top: 150px;
    display: flex; align-items: center; gap: 16px;
  }
  .brand-mark {
    width: 26px; height: 26px; background: var(--teal);
  }
  .brand-name {
    font-weight: 600; font-size: 38px; letter-spacing: 3px;
    color: var(--ink); text-transform: uppercase;
  }
  .person { position: absolute; left: 90px; top: 290px; }
  .person-name {
    font-weight: 600; font-size: 30px; color: var(--teal); letter-spacing: 0.5px;
  }
  .person-title {
    font-size: 19px; color: var(--text-dark); margin-top: 2px;
  }
  .contact-list {
    position: absolute; left: 90px; top: 378px; list-style: none;
  }
  .contact-item {
    display: flex; align-items: center; gap: 14px;
    font-size: 21px; line-height: 31px; color: var(--text-dark);
  }
  .contact-item svg { width: 20px; height: 20px; flex: none; fill: var(--teal); }
  .contact-item.address { align-items: flex-start; }
  .contact-item.address svg { margin-top: 5px; }
  .footer-rule {
    position: absolute; left: 0; right: 0; bottom: 64px; height: 6px; background: var(--teal);
  }
  .footer-band {
    position: absolute; left: 0; right: 0; bottom: 0; height: 64px; background: var(--band-dark);
  }
</style>
</head>
<body>
  <div class="card">
    <div class="brand">
      <span class="brand-mark"></span>
      <span class="brand-name">Pinecrest Renovations</span>
    </div>

    <div class="person">
      <div class="person-name">Marcus Hale</div>
      <div class="person-title">Managing Director</div>
    </div>

    <ul class="contact-list">
      <li class="contact-item">
        <svg viewBox="0 0 24 24"><path d="M6.6 10.8a15.1 15.1 0 0 0 6.6 6.6l2.2-2.2a1 1 0 0 1 1-.25 11.4 11.4 0 0 0 3.6.57 1 1 0 0 1 1 1V20a1 1 0 0 1-1 1A17 17 0 0 1 3 4a1 1 0 0 1 1-1h3.5a1 1 0 0 1 1 1c0 1.25.2 2.45.57 3.6a1 1 0 0 1-.25 1z"/></svg>
        (555) 410-2873
      </li>
      <li class="contact-item">
        <svg viewBox="0 0 24 24"><path d="M12 2a10 10 0 1 0 0 20 10 10 0 0 0 0-20zm6.9 6h-2.9a15.7 15.7 0 0 0-1.4-3.6A8 8 0 0 1 18.9 8zM12 4c.8 1.2 1.5 2.5 1.9 4h-3.8c.4-1.5 1.1-2.8 1.9-4zM4.3 14a8 8 0 0 1 0-4h3.4a16 16 0 0 0 0 4zm.8 2h2.9c.3 1.3.8 2.5 1.4 3.6A8 8 0 0 1 5.1 16zM8 8H5.1a8 8 0 0 1 4.3-3.6C8.8 5.5 8.3 6.7 8 8zm4 12c-.8-1.2-1.5-2.5-1.9-4h3.8c-.4 1.5-1.1 2.8-1.9 4zm2.3-6H9.7a14.7 14.7 0 0 1 0-4h4.6a14.7 14.7 0 0 1 0 4zm.3 5.6c.6-1.1 1.1-2.3 1.4-3.6h2.9a8 8 0 0 1-4.3 3.6zM16.3 14a16 16 0 0 0 0-4h3.4a8 8 0 0 1 0 4z"/></svg>
        www.pinecrestrenovations.com
      </li>
      <li class="contact-item">
        <svg viewBox="0 0 24 24"><path d="M3 5h18a1 1 0 0 1 1 1v12a1 1 0 0 1-1 1H3a1 1 0 0 1-1-1V6a1 1 0 0 1 1-1zm9 7.5L4.2 7h15.6zM4 8.6V17h16V8.6l-8 5.6z"/></svg>
        info@pinecrestrenovations.com
      </li>
      <li class="contact-item address">
        <svg viewBox="0 0 24 24"><path d="M12 3l10 9h-3v9h-5v-6h-4v6H5v-9H2z"/></svg>
        <span>Po Box 456, Harbor Street Belize,<br>NW 5120, Central America</span>
      </li>
    </ul>

    <div class="footer-rule"></div>
    <div class="footer-band"></div>
  </div>
</body>
</html>
```